Major Australian Food and Wine Event Web Design Project

The project will consist of 3 designs
The homepage
A city hub page
A general content page

The main audience who will visit the website will be (in Order of importance:

1) Visitors
- Mainly women 24 – 54 years (they are the main ticket buyers)
- In a relationship – so will go to the show with their partner
- In a good paying job or home maker – and who have disposable income to spend $30 a ticker
- Enjoy food, wine and going out
- Looking for a fun day out – although an event that is about food and wine – it is an event that most people will go to and have a fun day out – not too pretentious

A smaller proportion of the audience will be:
2) Exhibitors & sponsors ( both prospective and existing)
3) Media

Objectives:

- Functionality on home page and sub pages needs to be updated, clear, easy to navigate and inject a sense of ‘fun’ – need to make it look more professional
- Need to incorporate the many things that need to be on the home page and sub pages in a visually appealing manner
- Ensure the ‘Cons’ above are considered and reflected in functionality and design
- To not be too focus on the colours (these can be changed) – but focus on the functionality and overall design opportunities.

Approach:

Keywords to describe the Bright Table & Vine Fair:
Fun day out, discover, learn, indulge, entertaining

Other website examples:

Some great consumers event websites from the UK really make our website look basic and juvenile – and below are some examples of the presentation of how we would like our website to look like:

http://www.plumbazaar.example/london/ This website is clean, includes good social media integration and exudes a sense of fun. Their content pages, such as the features landing page also presents options in a clear and visually appealing way with a series of boxes including image and text http://www.plumbazaar.example/london/content/343/Features

http://www.hollowcraftexpo.example/ - this is also a great website – and it incorporates all the elements we would be looking for on our homepage – but the background/skin also includes a sense of fun and cheekiness. Subpages also are consistent.

Features

• Its a fun day that offers great value for money
• Caters to all visitors, regardless of different levels of knowledge or interest in food, wine and cooking.
• Sample great quality food and wine products from hundreds of reputable exhibitors
• Learn more through many of the shows feature activities (Celeb Theatre, Wine Theatre, Cooking & Cheese Classes)

Functionality & Structure:

In a user friendly, easy to view way, we need to incorporate the following functionality elements on home page:
- main header (that will incorporate our current creative) with a ‘fun’ skin
- navigation tabs/references (hone, location, tickets, blog, sign up, exhibitors)
- navigation/content banner (rotating)
- Area for small intro about the show
- News and highlight section
- New exhibitors section
- Obvious Ticket call to action
- Obvious sign up call to action
- Social media buttons or links ( really like the moving gifs on the Hollowcraftexpo.example site
- area for advertising (MREC size) to sell to exhibitors/sponsors
- Show dates for all 5 shows (maybe in main header)

Subpage layout is also important and needs to reflect the homepage – so would also like to see examples of how this would look and tie in with navigation – we generally have a lot of content on these pages, so clear navigation would be useful. – see below for further details of functionality for city Hubs

‘CITY HUB’ BRIEF
When navigating to each location the user will be taken to a ‘CITY HUB’ which should replicate design and content elements of a main HOME page, as well as reflect more specific information for each Show. Elements which must appear on this page are:
• FEATURES – which may be displayed in categories (in boxes, see appendix 1.0) which will link through to relevant content pages. Or in one box which will link through to a features page with all presented in boxes
• CHEFS – may be displayed as a separate icon box which will link to chefs page with bios, Celeb Theatre timetable etc.
• TICKETS – either a button or clear callout to purchase tickets
• PLAN YOUR DAY – may be displayed in a separate content box which will then link through to getting there, sample itineraries and downloadable pocket show guide for visitors to print before coming to the Show.
• WHO’S EXHIBITING – to link back to city specific exhibitor lists

Our current website is out of date and has the following inadequacies (www.brighttablefair.example.au) -

The homepage
A city hub page
A general content page

1) Visitors

3) Media

Objectives:

Approach:

To be perceived as a fun, entertaining event with something for everyone - website creative and navigation must reflect this.

Other website examples:

Features

- New exhibitors section

‘CITY HUB’ BRIEF

- Dated design/layout
- Homepage too text heavy
- No content boxes that can be used for different features/areas (eg. News, Exhibitors etc)
- Uninspiring colours and skin(eg. grey background), does not reflect ‘a fun day out’
- Limited presence of social media platforms and lacks ‘community’
- No continuity in sub pages
- main banner too big – takes up too much space on homepage

• As per above brief.

In addition:
Floating social media buttons on side
Wrap around image
Drop down menu (specifically for the location nav item)

```html
<!DOCTYPE html>
<html lang="en">
<head>
<meta charset="utf-8">
<title>Bright Table &amp; Vine Fair</title>
<link href="https://fonts.googleapis.com/css2?family=Roboto:wght@400;700&family=Roboto+Condensed:wght@400;700&family=Delius&family=Cinzel:wght@400&display=swap" rel="stylesheet">
<style>
:root{
  --ink:#1c1c1c;
  --black-bar:#1a1a1a;
  --orange:#e8551d;
  --orange-dark:#c23d10;
  --red:#d7261e;
  --navy:#163a6b;
  --gold:#fcc419;
  --gold-edge:#e0a200;
  --panel:#ffffff;
  --soft:#f1f1f1;
  --muted:#7a7a7a;
  --wood:#8a4a1c;
  --wood-dark:#4e2509;
  --sepia:#d8cfc0;
}
*{box-sizing:border-box;margin:0;padding:0}
html,body{width:928px;height:1200px;overflow:hidden}
body{position:relative;font-family:"Roboto",Arial,sans-serif;color:var(--ink);font-size:8px;
  background:linear-gradient(180deg,#f3efe8 0%,#e7dfd2 30%,#cfc4b2 55%,#e9e4dc 80%,#f2efea 100%)}
.abs{position:absolute}
.scenery{position:absolute;left:0;top:92px;width:928px;height:930px;
  background:radial-gradient(ellipse at 15% 45%,#b8ab96 0%,transparent 45%),radial-gradient(ellipse at 90% 40%,#b9ad98 0%,transparent 40%),linear-gradient(180deg,transparent 0%,rgba(160,145,120,.35) 35%,transparent 75%)}
/* header */
.topbar{left:0;top:0;width:928px;height:62px;background:linear-gradient(#333,#0f0f0f)}
.navbar{left:0;top:62px;width:928px;height:30px;background:linear-gradient(#f06a2a,#d44812)}
.brand{left:106px;top:0;width:129px;height:108px;background:#fff;border-radius:0 0 16px 16px;box-shadow:0 2px 6px rgba(0,0,0,.25);display:flex;align-items:center;justify-content:center;text-align:center}
.brand-name{font-family:"Delius",cursive;font-size:17px;line-height:1.15;color:#222;width:110px}
.event-title{left:330px;top:20px;font-family:"Delius",cursive;font-size:19px;color:#fff;letter-spacing:.3px}
.call-btn{left:680px;top:22px;width:142px;height:24px;background:var(--gold);border:1px solid var(--gold-edge);border-radius:3px;font-family:"Roboto Condensed",sans-serif;font-size:12px;line-height:22px;text-align:center;color:#222}
.main-nav{left:326px;top:62px;display:flex;height:30px}
.main-nav a{font-family:"Roboto Condensed",sans-serif;font-weight:700;font-size:9.5px;color:#fff;text-decoration:none;line-height:30px;padding:0 9px}
.main-nav a.active{background:#8b2a0c;position:relative}
.main-nav a.active::after{content:"";position:absolute;left:50%;bottom:-6px;margin-left:-6px;border:6px solid transparent;border-top-color:#8b2a0c;border-bottom:0}
.tagline{left:108px;top:136px;font-family:"Roboto Condensed",sans-serif;font-size:14px;line-height:17px}
.tagline .red{color:var(--red)}
.tagline .blue{color:var(--navy)}
.plate{top:118px;width:100px;height:100px;border-radius:50%}
/* main panel */
.panel{left:92px;top:194px;width:744px;height:804px;background:var(--panel);border-radius:0 0 18px 18px;box-shadow:0 2px 8px rgba(0,0,0,.2)}
.slider{left:99px;top:209px;width:487px;height:189px;background:#cfcac0;padding:6px}
.slider-art{width:100%;height:100%;background:linear-gradient(90deg,#7a2a1a 0%,#a2452c 30%,#f4f1ec 55%,#e9e6e0 100%)}
.slider-caption{left:110px;top:357px;width:469px;height:35px;background:rgba(40,40,40,.78);font-family:"Cinzel",serif;font-size:14px;color:#fff;line-height:35px;padding-left:14px;letter-spacing:.5px}
.dots{position:absolute;right:12px;top:13px;display:flex;gap:5px}
.dots i{width:7px;height:7px;border-radius:50%;background:#fff;display:block}
.dots i:first-child{background:transparent;border:1.5px solid #fff}
.wine-promo{left:599px;top:209px;width:235px;height:189px;background:linear-gradient(135deg,#efe2b8,#e6d39a 60%,#d9c488)}
.wine-promo h3{position:absolute;left:12px;top:12px;font-family:"Roboto",sans-serif;font-weight:700;font-size:11.5px;line-height:12.5px;color:#1e1e1e;letter-spacing:.2px}
.wine-promo p{position:absolute;left:12px;top:57px;font-size:9px;line-height:12px;width:110px}
.btn{display:inline-block;background:var(--gold);border:1px solid var(--gold-edge);border-radius:3px;font-size:9.5px;color:#222;line-height:18px;padding:0 10px}
.wine-promo .btn{position:absolute;left:12px;top:94px;font-size:11px;line-height:18px;padding:0 12px}
.wine-art{position:absolute;left:120px;top:55px;width:108px;height:128px;background:linear-gradient(90deg,rgba(120,110,70,.35),rgba(255,250,225,.6));border-radius:4px}
.partner-mark{position:absolute;left:8px;top:140px;width:64px;height:38px;background:#fff;display:flex;align-items:center;justify-content:center;font-size:10px;color:#222}
.intro{left:108px;top:416px;width:478px}
.intro h1{font-family:"Roboto Condensed",sans-serif;font-weight:400;font-size:15px;color:var(--navy);padding-bottom:8px;border-bottom:1px solid #ccc}
.intro h1 span{color:var(--red)}
.intro p{font-size:8px;line-height:12.4px;color:#333;margin-top:10px}
.intro ul{list-style:none;margin-top:9px}
.intro li{font-size:8px;line-height:15.5px;color:var(--navy);padding-left:10px;position:relative}
.intro li::before{content:"";position:absolute;left:0;top:4px;border:3.5px solid transparent;border-left:5px solid var(--navy);border-right:0}
.intro .signup{font-size:9px;color:#111;margin-top:12px}
.news{left:599px;top:414px;width:221px;height:212px;background:var(--soft);padding:10px 12px}
.news h2{font-family:"Roboto Condensed",sans-serif;font-weight:700;font-size:14.5px;color:var(--red)}
.news .sub{font-family:"Roboto Condensed",sans-serif;font-size:11px;color:var(--muted);margin-top:1px}
.news p{font-size:8px;line-height:12.3px;color:#444;margin-top:9px}
.news .more{font-size:9px;color:#111;margin-top:6px}
.news .btn{position:absolute;right:12px;bottom:14px}
.tickets-tab{left:52px;top:406px;width:38px;height:138px;background:linear-gradient(90deg,#f39a35,#ea7c1c);border-radius:6px 0 0 6px;border:2px solid #fff;border-right:0}
.tickets-tab span{position:absolute;left:50%;top:50%;transform:translate(-50%,-50%) rotate(-90deg);white-space:nowrap;font-family:"Roboto",sans-serif;font-weight:700;font-size:12.5px;color:#fff;letter-spacing:.5px}
.social-tab{left:836px;top:406px;width:40px;height:138px;background:linear-gradient(90deg,#ea7c1c,#f39a35);border-radius:0 6px 6px 0;padding:6px 0 0 6px}
.social-tab i{display:block;width:27px;height:27px;border-radius:4px;background:#fff;opacity:.9;margin-bottom:5px;border:1px solid #d66a10}
/* columns */
.rule{top:640px;height:5px;border-top:2px solid var(--red);border-bottom:1px solid var(--red)}
.col-tab{top:660px;height:24px;background:var(--red);color:#fff;font-weight:700;font-size:10.5px;line-height:24px;padding:0 9px;width:105px}
.col-box{top:684px;width:235px;height:298px;border:1px solid #ddd;padding:7px}
.item{height:78px;background:var(--soft);margin-bottom:8px;position:relative;padding:10px 0 0 10px}
.item p{font-size:7.8px;line-height:12.3px;color:#444;width:120px}
.item .more{font-size:9px;color:#111;margin-top:6px}
.thumb{position:absolute;right:9px;top:11px;width:71px;height:57px;border:1px solid #bbb}
.col-box .btn{position:absolute;right:9px;bottom:9px}
.foodie{left:599px;top:660px;width:221px;height:154px;background:linear-gradient(180deg,#b3a79a,#7d6e60 60%,#3e3330)}
.foodie span{position:absolute;left:12px;bottom:14px;font-weight:700;font-size:11.5px;line-height:14px;color:#fff;letter-spacing:.3px}
.advert{left:599px;top:828px;width:221px;height:153px;background:linear-gradient(180deg,#f3f3f3,#ececec);display:flex;align-items:center;justify-content:center}
.advert div{width:150px;height:100px;border-radius:6px;background:rgba(255,255,255,.65);border:1px solid #ddd;display:flex;align-items:center;justify-content:center;font-family:"Roboto Condensed",sans-serif;font-size:14px;color:#888}
/* footer */
.footer{left:0;top:1022px;width:928px;height:178px;background:repeating-linear-gradient(90deg,#7c3f14 0,#9a5422 18px,#84461a 40px,#6e3510 58px,#92511f 80px)}
.footer::before{content:"";position:absolute;inset:0;background:radial-gradient(ellipse at 50% 40%,rgba(210,120,50,.35),transparent 70%)}
.foot-col{top:1045px}
.foot-col h4{font-family:"Roboto Condensed",sans-serif;font-weight:700;font-size:10.5px;color:#fff;margin-bottom:8px;letter-spacing:.2px}
.foot-col a{display:block;font-size:9px;color:#fff;line-height:15.5px;text-decoration:none}
.newsletter{left:599px;top:1047px;width:221px;height:129px;background:rgba(40,20,6,.82);border-radius:6px;padding:10px 15px}
.newsletter h4{font-family:"Roboto Condensed",sans-serif;font-size:14.5px;font-weight:400;color:#fff}
.newsletter p{font-size:7.8px;line-height:11px;color:#fff;margin-top:8px}
.newsletter .field{margin-top:9px;width:157px;height:18px;background:#fff;font-size:7.5px;color:#999;padding:4px 7px}
.newsletter .go{margin-top:10px;font-weight:700;font-size:10px;color:var(--gold)}
.legal{top:1168px;font-size:7.8px;color:#fff}
</style>
</head>
<body>
<div class="scenery" role="img" aria-label="Faded sepia vineyard landscape wrapping behind the page"></div>

<header>
  <div class="abs topbar"></div>
  <div class="abs navbar"></div>
  <div class="abs brand"><div class="brand-name">Bright Table &amp; Vine Fair</div></div>
  <div class="abs event-title">Major Australian Food and Wine Event</div>
  <div class="abs call-btn">Call Now : 613 5550 2178</div>
  <nav class="abs main-nav">
    <a class="active" href="#">HOME</a><a href="#">LOCATION</a><a href="#">TICKETS</a><a href="#">BLOG</a><a href="#">SIGN UP</a><a href="#">EXHIBITORS</a><a href="#">RECIPE CLUB</a><a href="#">CONTACT US</a>
  </nav>
  <div class="abs tagline"><div class="red">Looking for a fun day out</div><div class="blue">An event that is about food and wine...</div></div>
  <div class="abs plate" style="left:360px;background:radial-gradient(circle,#e8401c 40%,#d8d2c8 42%)" role="img" aria-label="Tomato in a plate recess"></div>
  <div class="abs plate" style="left:470px;background:radial-gradient(circle,#5a7a3a 30%,#161616 40%,#d8d2c8 42%)" role="img" aria-label="Pan of stir-fried seafood"></div>
  <div class="abs plate" style="left:588px;background:radial-gradient(circle,#e9c9a0 38%,#d8d2c8 42%)" role="img" aria-label="Plate of sushi rolls"></div>
  <div class="abs plate" style="left:702px;background:radial-gradient(circle,#d9a23a 18%,#2d4a4a 38%,#d8d2c8 42%)" role="img" aria-label="Decorated dish"></div>
</header>

<main>
  <div class="abs panel"></div>

  <div class="abs slider"><div class="slider-art" role="img" aria-label="Glazed meat dish with lime beside two smiling chefs"></div></div>
  <div class="abs slider-caption">SUCCUMB TO YOUR SENSES<div class="dots"><i></i><i></i><i></i><i></i><i></i></div></div>

  <section class="abs wine-promo">
    <h3>INDULGE YOUR PASSION<br>FOR REGIONAL PREMIUM WINES</h3>
    <p>Sip into the Vellaro Wine Theatre - 2012</p>
    <span class="btn">Click here</span>
    <div class="wine-art" role="img" aria-label="Bottle of sparkling wine with two filled flutes"></div>
    <div class="partner-mark">Vellaro</div>
  </section>

  <section class="abs intro">
    <h1><span>The Bright Table &amp; Vine Fair</span> - All over for another year!</h1>
    <p>Melbourne, Sydney, Perth, Adelaide and Brisbane have all had the chance to experience the fun, excitement and joy, that is the Bright Table &amp; Vine Fair! We would like to thank all our amazing visitors for coming along and helping us celebrate another awesome year A big thank you also to the rest of the crew including exhibitors, sponsors and chefs!</p>
    <ul>
      <li>Its a fun day that offers great value for money</li>
      <li>Caters to all visitors, regardless of different levels of knowledge or interest in food, wine and cooking.</li>
      <li>Sample great quality food and wine products from hundreds of reputable exhibitors</li>
      <li>Learn more through many of the shows feature activities (Celeb Theatre, Wine Theatre, Cooking &amp; Cheese Classes)</li>
    </ul>
    <p>Make sure you visit the website early next year for all the details of the 2012 Shows - or sign up to our newsletter to be the first to find out when we are on sale and to receive special discounts and offers!</p>
    <div class="signup">Sign up to the Bright Table &amp; Vine Fair e-newsletter</div>
  </section>

  <section class="abs news">
    <h2>News &amp; Media Releases</h2>
    <div class="sub">Bright Table &amp; Vine Fair</div>
    <p>Lorem Ipsum is simply dummy text of the printing and typesetting industry. Lorem Ipsum has been the industry's standard dummy text.</p>
    <div class="more">Read more</div>
    <p>Lorem Ipsum is simply dummy text of the printing and typesetting industry. Lorem Ipsum has been the industry's standard dummy text.</p>
    <div class="more">Read more</div>
    <span class="btn">Click here for more</span>
  </section>

  <div class="abs tickets-tab"><span>BOOK TICKETS</span></div>
  <div class="abs social-tab" aria-label="Social links"><i></i><i></i><i></i><i></i></div>

  <div class="abs rule" style="left:106px;width:234px"></div>
  <div class="abs rule" style="left:353px;width:233px"></div>
  <div class="abs rule" style="left:599px;width:221px"></div>

  <div class="abs col-tab" style="left:106px">HIGHLIGHTS</div>
  <section class="abs col-box" style="left:106px">
    <div class="item"><p>Lorem Ipsum is simply dummy text of the printing and type setting industry.</p><div class="more">Read more</div><div class="thumb" style="background:linear-gradient(135deg,#c23a2a,#e8d8cc)" role="img" aria-label="Visitors tasting food"></div></div>
    <div class="item"><p>Lorem Ipsum is simply dummy text of the printing and type setting industry.</p><div class="more">Read more</div><div class="thumb" style="background:linear-gradient(135deg,#6a6a6a,#e6e6e6)" role="img" aria-label="Chefs cooking on stage"></div></div>
    <div class="item"><p>Lorem Ipsum is simply dummy text of the printing and type setting industry.</p><div class="more">Read more</div><div class="thumb" style="background:linear-gradient(135deg,#1d1d1d,#7b6a4a)" role="img" aria-label="Wine theatre stage"></div></div>
    <span class="btn">View all Highlights</span>
  </section>

  <div class="abs col-tab" style="left:353px">EXHIBITORS</div>
  <section class="abs col-box" style="left:353px">
    <div class="item"><p>Lorem Ipsum is simply dummy text of the printing and type setting industry.</p><div class="more">Read more</div><div class="thumb" style="background:linear-gradient(135deg,#6e7a6a,#cfc6b4)" role="img" aria-label="Exhibitor stand"></div></div>
    <div class="item"><p>Lorem Ipsum is simply dummy text of the printing and type setting industry.</p><div class="more">Read more</div><div class="thumb" style="background:linear-gradient(135deg,#3a2a2a,#d8262a 60%,#fff)" role="img" aria-label="Busy exhibitor hall"></div></div>
    <div class="item"><p>Lorem Ipsum is simply dummy text of the printing and type setting industry.</p><div class="more">Read more</div><div class="thumb" style="background:linear-gradient(135deg,#4d6a8a,#e0c060)" role="img" aria-label="Product display counter"></div></div>
    <span class="btn">View all Exhibitors</span>
  </section>

  <div class="abs foodie" role="img" aria-label="Crowd at a cooking demonstration"><span>INDULGE ALL YOUR FOODIE<br>FANTASIES</span></div>
  <div class="abs advert"><div>Area for Advertising</div></div>
</main>

<footer>
  <div class="abs footer" role="img" aria-label="Wooden plank backdrop"></div>
  <div class="abs foot-col" style="left:108px"><h4>BRIGHT TABLE LOCATIONS</h4><a>Melbourne</a><a>Sydney</a><a>Perth</a><a>Adelaide</a><a>Brisbane</a></div>
  <div class="abs foot-col" style="left:264px"><h4>SHOW AND ATTRACTIONS</h4><a>Tickets</a><a>Blog</a><a>Exhibitor list</a><a>Recipe Club</a><a>Restaurant / Wine</a></div>
  <div class="abs foot-col" style="left:428px"><h4>BRIGHT TABLE CHEF BIO'S</h4><a>Nora Pell</a><a>Dane Whitcombe</a><a>Theo Marandis</a><a>Luc Ravenel</a><a>Sam Corrigan</a></div>
  <section class="abs newsletter">
    <h4>Newsletter Signup</h4>
    <p>Signup to our newsletter and receive any updates on the any kind of events.</p>
    <div class="field">Your E-mail Address here</div>
    <div class="go">SUBSCRIBE NOW</div>
  </section>
  <div class="abs legal" style="left:108px">© Copyright 2012 Bright Table &amp; Vine Fair.</div>
  <div class="abs legal" style="left:324px">Website Design &amp; Developed : www.tidewaystudio.example</div>
</footer>
</body>
</html>
```